Startup online payment business - Sporting / Golf, Swift Tee payment

Background:
Our business name is "Swift Tee" we provide online payments for golfing services via our website. We currently have a logo used on our website. No other design style has been developed. Our aim is to remove cash payments for service at golf clubs.

Our Key Values:
Quick and easy
Formal and polite
Fun with professional boundary
Mate-ship relationships
100% online digital

What we want from you:
Marketing design to be used on posters and stickers in a retail setting to direct customers to our online payment Chanel.
Design must incorporate attached logo, URL swifttee.com.au and our key values can act as a guide the type of design. We have used color Hex#007672 for logo background. We are open to use other colors.

Target Market(s)

Golf clubs and golf players

Industry/Entity Type

Golf Course

Font styles to use
Sans Serif

Requirements
Must have
• Directions to online payment via URL: swifttee.com.au
Nice to have
• We like the idea of the slogan: No Cash - No worries. Have attached home screen that will be available from URL link. Consideration if using mobile phone in image. Push the online payment and steps 1. Visit swifttee.com 2. Select club 3. Confirm payment
Should not have
• Cartoons

```html
<!DOCTYPE html>
<html lang="en">
<head>
<meta charset="utf-8">
<title>Swift Tee – No Cash, No Worries</title>
<link rel="stylesheet" href="https://fonts.googleapis.com/css2?family=Open+Sans:ital,wght@0,400;0,700;0,800;1,400;1,600&family=Ubuntu:wght@500&display=swap">
<style>
  :root{
    --teal:#1e8f63;
    --teal-deep:#187a55;
    --lime:#6cd200;
    --cream:#f8fbbf;
    --grass:#6fbd1f;
    --white:#ffffff;
    --paper:#ffffff;
  }
  *{margin:0;padding:0;box-sizing:border-box}
  html,body{width:824px;height:1200px;overflow:hidden;background:var(--paper)}
  .canvas{position:relative;width:824px;height:1200px;font-family:"Open Sans",sans-serif}
  .poster{position:absolute;left:44px;top:32px;width:770px;height:1114px;background:var(--cream);overflow:hidden}
  .course-photo{position:absolute;left:0;top:680px;width:770px;height:434px;
    background:linear-gradient(180deg,rgba(248,251,191,0) 0%,#d9ec8a 22%,#b7db5a 45%,#8fcb34 70%,var(--grass) 100%)}
  .club-photo{position:absolute;left:400px;top:900px;width:370px;height:180px;
    background:radial-gradient(ellipse at 45% 65%,rgba(235,235,235,.9) 0 12%,rgba(160,168,160,.6) 30%,rgba(120,140,110,0) 62%)}
  .frame{position:absolute;left:50px;top:30px;width:673px;height:1056px;border:2px solid var(--white)}
  .shapes{position:absolute;left:0;top:0}
  .brand-name{position:absolute;left:37px;top:62px;width:221px;text-align:center;color:var(--white);
    font-weight:800;font-size:34px;letter-spacing:3px;text-transform:uppercase}
  .values-title{position:absolute;left:69px;top:198px;color:var(--teal);font-weight:700;font-size:31px;
    text-decoration:underline;text-decoration-thickness:2px;text-underline-offset:4px;letter-spacing:-.5px}
  .values{position:absolute;left:66px;top:254px;list-style:none}
  .value{display:flex;align-items:center;height:41px;color:var(--teal);font-family:"Ubuntu",sans-serif;font-weight:500;font-size:23px;letter-spacing:.3px}
  .value svg{flex:none}
  .value .arrow{margin:0 10px 0 14px}
  .promise{position:absolute;right:68px;top:78px;text-align:right;color:var(--white);font-style:italic;font-weight:600;font-size:23px;line-height:35px}
  .digital-pct{position:absolute;left:555px;top:313px;width:180px;text-align:center;color:var(--white);font-weight:700;font-size:27px;line-height:34px}
  .digital-label{position:absolute;left:555px;top:399px;width:180px;text-align:center;color:var(--white);font-style:italic;font-size:20px;line-height:30px}
  .phone{position:absolute;left:43px;top:440px;width:124px;height:257px;border-radius:18px;
    background:linear-gradient(180deg,#f2f4f4,#dfe3e3);border:2px solid #cfd5d5}
  .phone-screen{position:absolute;left:5px;top:30px;width:110px;height:196px;background:var(--teal-deep)}
  .steps{position:absolute;left:186px;top:498px;color:var(--white)}
  .steps-title{font-weight:800;font-size:26px;letter-spacing:-.5px}
  .steps-list{list-style:none;margin-top:18px}
  .steps-list li{font-size:20px;height:37px;display:flex}
  .steps-list .num{width:33px}
  .slogan{position:absolute;left:0;width:770px;top:740px;text-align:center;color:var(--teal);
    font-weight:800;font-size:36px;font-variant:small-caps;letter-spacing:3px}
  .url-pill{position:absolute;left:166px;top:829px;width:438px;height:54px;border-radius:27px;background:var(--teal);
    color:var(--white);font-weight:800;font-size:25px;letter-spacing:13px;display:flex;align-items:center;justify-content:center;padding-left:13px}
</style>
</head>
<body>
<div class="canvas">
  <div class="poster">
    <div class="course-photo" role="img" aria-label="Blurred golf course fairway with green grass"></div>
    <div class="club-photo" role="img" aria-label="Golf iron resting behind a golf ball on the grass"></div>
    <div class="frame"></div>

    <svg class="shapes" width="770" height="1114" viewBox="0 0 770 1114" aria-hidden="true">
      <path d="M398 110 Q380 118 400 145 L510 265 Q530 280 560 272 L665 243 L770 220 L770 110 Z" fill="var(--teal)"/>
      <path d="M420 58 L770 58 L770 240 L505 240 Q480 240 465 220 L400 110 Q390 85 420 58 Z" fill="var(--lime)"/>
      <path d="M600 310 L770 310 L770 434 L530 434 Q515 434 522 422 L590 320 Q595 310 600 310 Z" fill="var(--teal)"/>
      <circle cx="645" cy="372" r="25" fill="var(--lime)" stroke="var(--white)" stroke-width="2"/>
      <rect x="636" y="360" width="15" height="24" rx="3" fill="none" stroke="var(--white)" stroke-width="2"/>
      <path d="M646 368 h12 M646 374 h9" stroke="var(--white)" stroke-width="2"/>
      <path d="M270 528 L700 528 Q720 530 710 555 L620 700 Q600 718 570 715 L150 700 L150 660 Z" fill="var(--teal)"/>
      <path d="M0 486 L685 486 Q705 490 695 510 L600 670 Q590 680 560 680 L0 680 Z" fill="var(--lime)"/>
      <path d="M37 0 L258 0 L258 165 Q258 185 240 178 Q150 150 60 178 Q37 185 37 165 Z" fill="var(--teal)"/>
    </svg>

    <div class="brand-name">Swift Tee</div>

    <h2 class="values-title">Our Key Values:</h2>
    <ul class="values">
      <li class="value">
        <svg width="34" height="34" viewBox="0 0 34 34" fill="none" stroke="currentColor" stroke-width="2"><circle cx="19" cy="19" r="11"/><path d="M19 13v6l4 3M17 5h4M19 5v3M2 16h6M4 21h5"/></svg>
        <svg class="arrow" width="26" height="12" viewBox="0 0 26 12"><path d="M0 0 L26 6 L0 12 L5 6 Z" fill="currentColor"/></svg>Quick and easy</li>
      <li class="value">
        <svg width="34" height="34" viewBox="0 0 34 34" fill="none" stroke="currentColor" stroke-width="2"><path d="M13 3h8v5h-8zM13 8l-3 18 7 6 7-6-3-18M12 15l10-4M11 21l12-4"/></svg>
        <svg class="arrow" width="26" height="12" viewBox="0 0 26 12"><path d="M0 0 L26 6 L0 12 L5 6 Z" fill="currentColor"/></svg>Formal and polite</li>
      <li class="value">
        <svg width="34" height="34" viewBox="0 0 34 34" fill="none" stroke="currentColor" stroke-width="2"><path d="M10 12l14 8-11 5z"/><path d="M6 6l2 2M27 6l-2 3M29 14h-3M5 20h3M8 28l2-2"/></svg>
        <svg class="arrow" width="26" height="12" viewBox="0 0 26 12"><path d="M0 0 L26 6 L0 12 L5 6 Z" fill="currentColor"/></svg>Fun with professional boundary</li>
      <li class="value">
        <svg width="34" height="34" viewBox="0 0 34 34" fill="none" stroke="currentColor" stroke-width="2"><circle cx="11" cy="9" r="5"/><circle cx="23" cy="9" r="5"/><path d="M3 31v-9q0-6 8-6t8 6v9M17 22q0-6 6-6t8 6v9H3"/></svg>
        <svg class="arrow" width="26" height="12" viewBox="0 0 26 12"><path d="M0 0 L26 6 L0 12 L5 6 Z" fill="currentColor"/></svg>Mate-ship relationships</li>
    </ul>

    <p class="promise">We provide<br>online payments<br>for golfing services<br>via our website</p>

    <div class="digital-pct">100%</div>
    <div class="digital-label">Online Digital</div>

    <div class="phone" role="img" aria-label="Mobile phone showing the Swift Tee payment home screen">
      <div class="phone-screen"></div>
    </div>

    <div class="steps">
      <h3 class="steps-title">To pay online, just follow three steps:</h3>
      <ol class="steps-list">
        <li><span class="num">1.</span>Visit swifttee.com.au</li>
        <li><span class="num">2.</span>Select club</li>
        <li><span class="num">3.</span>Confirm payment</li>
      </ol>
    </div>

    <p class="slogan">No Cash-No Worries</p>
    <div class="url-pill">swifttee.com.au</div>
  </div>
</div>
</body>
</html>
```